Tova Brisk Fitness Coaching Project

I am a personal trainer based in London. My services include one-on-one PT sessions, bootcamps.
I would like the design to be minimalistic. With light colours: white, pink, purple.
I specialise in weight loss, flexibility, mobility.

Tova Penrick
Personal Trainer
Email: tova.penrick@mailgrove.net
tel: 07500 918 243
Instagram: Tova Brisk

Target Market(s)

adults, mostly females (age 18-50).

Industry/Entity Type

Fitness

Contact Information for Business Card

Tova Penrick
Personal Trainer
tel: 07500 918 243
Instagram: Tova Brisk

Font styles to use
Serif

Colors
eea4c8
fbd4d5
fdf9cf
cfeae6
cee9f5

Requirements
Nice to have
• minimalistic style
• easy to read and remember

```html
<!DOCTYPE html>
<html lang="en">
<head>
<meta charset="utf-8">
<title>Tova Penrick – Personal Trainer Business Card</title>
<link href="https://fonts.googleapis.com/css2?family=Yellowtail&family=Tinos:wght@400&display=swap" rel="stylesheet">
<style>
  :root {
    --backdrop: #ecebee;
    --frame-pink: #e8a6cf;
    --photo-border: #fdfbfc;
    --sky: #d4e9f5;
    --band-white: #ffffff;
    --band-pink: #f7c9cc;
    --ink: #2a2a33;
    --accent: #c0609f;
    --icon: #b05a93;
    --wall-coral: #e57a66;
    --wall-peach: #f2a08b;
    --mural-magenta: #e0237f;
    --mural-teal: #3cb8c4;
  }
  * { box-sizing: border-box; margin: 0; padding: 0; }
  html, body { width: 1200px; height: 852px; overflow: hidden; }
  body {
    background: var(--backdrop);
    position: relative;
    font-family: "Tinos", "Times New Roman", serif;
  }
  .card {
    position: absolute;
    top: 271px;
    width: 540px;
    height: 310px;
    border-radius: 22px;
    overflow: hidden;
    box-shadow: 0 10px 28px rgba(40, 30, 50, 0.18);
  }
  /* Back side */
  .card--back {
    left: 40px;
    background: var(--frame-pink);
    padding: 18px;
    display: flex;
    gap: 10px;
  }
  .photo-slot {
    height: 100%;
    border: 4px solid var(--photo-border);
  }
  .photo-slot--doorway {
    flex: 0 0 196px;
    background: linear-gradient(160deg, var(--wall-peach) 0%, var(--wall-coral) 60%, #7a5a4a 100%);
  }
  .photo-slot--mural {
    flex: 1;
    background: linear-gradient(170deg, var(--mural-magenta) 0%, var(--mural-magenta) 40%, var(--mural-teal) 62%, #3a4a50 90%);
  }
  /* Front side */
  .card--front {
    left: 620px;
    background: var(--sky);
  }
  .card-art { position: absolute; inset: 0; }
  .photo-mural-front {
    position: absolute; inset: 0;
  }
  .identity {
    position: absolute;
    left: 62px;
    top: 82px;
  }
  .identity__name {
    font-family: "Yellowtail", cursive;
    font-size: 38px;
    font-weight: 400;
    color: var(--ink);
    line-height: 1;
  }
  .identity__role {
    font-size: 13px;
    color: var(--accent);
    margin: 4px 0 12px 4px;
  }
  .contact-list { list-style: none; margin-left: 18px; }
  .contact-list li {
    display: flex;
    align-items: center;
    gap: 8px;
    font-size: 13.5px;
    color: var(--ink);
    height: 22px;
  }
  .contact-icon { width: 16px; height: 16px; flex: 0 0 16px; }
</style>
</head>
<body>

  <section class="card card--back" aria-label="Business card back">
    <div class="photo-slot photo-slot--doorway" role="img" aria-label="Photo of the trainer doing a handstand in front of a coral house doorway"></div>
    <div class="photo-slot photo-slot--mural" role="img" aria-label="Photo of the trainer leaping in front of a pink and teal painted wall"></div>
  </section>

  <section class="card card--front" aria-label="Business card front">
    <svg class="card-art" viewBox="0 0 540 310" width="540" height="310" aria-hidden="true">
      <defs>
        <linearGradient id="muralTones" x1="0" y1="0" x2="0.3" y2="1">
          <stop offset="0" stop-color="#e0237f"/>
          <stop offset="0.38" stop-color="#e0237f"/>
          <stop offset="0.5" stop-color="#3cb8c4"/>
          <stop offset="0.85" stop-color="#37a8b2"/>
          <stop offset="1" stop-color="#2f4f55"/>
        </linearGradient>
      </defs>
      <path d="M205 0 Q250 160 150 310 L540 310 L540 0 Z" fill="var(--band-white)"/>
      <path d="M232 0 Q275 170 205 310 L540 310 L540 0 Z" fill="var(--band-pink)"/>
      <path d="M244 0 Q290 170 252 310 L540 310 L540 0 Z" fill="var(--band-white)"/>
      <path d="M256 0 Q305 170 262 310 L540 310 L540 0 Z" fill="url(#muralTones)" role="img" aria-label="Photo of the trainer in a low lunge in front of a pink and teal mural"/>
    </svg>

    <div class="identity">
      <h1 class="identity__name">Tova Penrick</h1>
      <p class="identity__role">Personal Trainer</p>
      <ul class="contact-list">
        <li>
          <svg class="contact-icon" viewBox="0 0 16 16" aria-hidden="true">
            <circle cx="8" cy="8" r="7.2" fill="none" stroke="var(--icon)" stroke-width="1.2"/>
            <path d="M5.2 4.4h1.6l.7 1.8-1 .7a5 5 0 0 0 2.6 2.6l.7-1 1.8.7v1.6c0 .5-.4.8-.9.8A6.3 6.3 0 0 1 4.4 5.3c0-.5.3-.9.8-.9z" fill="var(--icon)"/>
          </svg>
          07500 918 243
        </li>
        <li>
          <svg class="contact-icon" viewBox="0 0 16 16" aria-hidden="true">
            <circle cx="8" cy="8" r="7.2" fill="none" stroke="var(--icon)" stroke-width="1.2"/>
            <rect x="4" y="5.2" width="8" height="5.6" rx="0.8" fill="var(--icon)"/>
            <path d="M4.4 5.6 8 8.4l3.6-2.8" fill="none" stroke="#fff" stroke-width="0.9"/>
          </svg>
          tova.penrick@mailgrove.net
        </li>
        <li>
          <svg class="contact-icon" viewBox="0 0 16 16" aria-hidden="true">
            <circle cx="8" cy="8" r="7.2" fill="none" stroke="var(--icon)" stroke-width="1.2"/>
          </svg>
          Tova Brisk
        </li>
      </ul>
    </div>
  </section>

</body>
</html>
```